Brivon Australia Dental

I need to update my website and design. I have some ideas in mind and would like to replicate the format from another website into my own. I need the website to be easy to edit (I have no prior wordpress exp) after the design is complete. Please visit https://thelittlenestcare.org.au/ for example of layout.
Target Market(s)
Parents and elder folks
Industry/Entity Type
Dental
Coding
Coded - Design and coding required
Number of Pages Required
4 page
Font styles to use
Sans Serif
Colors
0392cd
Requirements
Must have
- - Home, Services, About Us, News
- - Colours
- - Clear action from viewers
- - Location of business (able to change all the time)
- - Illustrations/ photos

```html
<!DOCTYPE html>
<html lang="en">
<head>
<meta charset="utf-8">
<title>Brivon Australia Dental</title>
<link href="https://fonts.googleapis.com/css2?family=Fira+Sans:wght@300;400;500;700;800&display=swap" rel="stylesheet">
<style>
:root{
  --blue:#0392cd;
  --blue-dark:#027bb0;
  --ink:#2a2a2e;
  --body:#7a7a7a;
  --line:#e6e6e6;
  --footer:#262a33;
  --white:#ffffff;
}
*{box-sizing:border-box;margin:0;padding:0}
html,body{width:1200px;height:3720px;overflow:hidden}
body{position:relative;background:var(--white);font-family:"Fira Sans",Arial,sans-serif;color:var(--ink)}
.abs{position:absolute}
.btn{position:absolute;display:flex;align-items:center;justify-content:center;border-radius:22px;font-weight:500;font-size:15px;text-decoration:none}
.btn-blue{background:var(--blue);color:var(--white)}
.btn-white{background:var(--white);color:var(--blue)}
.logo{font-family:"Fira Sans",Arial,sans-serif;font-weight:500;font-size:34px;letter-spacing:.5px;line-height:1}

/* top bar & nav */
.topbar{top:0;left:0;width:1200px;height:33px;border-bottom:1px solid var(--line)}
.topbar-phone{left:94px;top:8px;font-size:13px;color:var(--blue);display:flex;align-items:center;gap:4px}
.nav-logo{left:94px;top:46px;color:var(--blue)}
.nav{top:56px;display:flex;font-size:12px;color:#555}
.nav a{position:absolute;color:#555;text-decoration:none;white-space:nowrap}
.nav a.active{color:var(--blue)}

/* hero */
.hero{top:94px;left:0;width:1200px;height:497px;background:linear-gradient(90deg,#c2bdb8 0%,#d3d6e6 38%,#c7d0ee 62%,#b4c0e4 100%)}
.hero-small{left:544px;top:258px;font-size:43px;font-weight:500;color:var(--white)}
.hero-big{left:544px;top:306px;font-size:80px;font-weight:700;color:var(--white);letter-spacing:.5px;line-height:1}
.hero-btn{left:543px;top:414px;width:199px;height:42px}
.dot{top:547px;width:12px;height:12px;border-radius:50%;border:2px solid rgba(255,255,255,.8)}
.dot.on{background:var(--blue);border-color:var(--blue)}

/* booking */
.booking{left:94px;top:552px;width:394px;height:548px;background:var(--blue);border-radius:6px;box-shadow:0 6px 18px rgba(0,0,0,.12)}
.booking-small{left:26px;top:46px;font-size:32px;font-weight:300;color:var(--white)}
.booking-big{left:26px;top:80px;font-size:46px;font-weight:700;color:var(--white)}
.field{position:absolute;left:26px;width:342px;height:36px;border:1.5px solid rgba(255,255,255,.85);border-radius:18px;color:var(--white);font-size:11px;padding:11px 12px}
.field.area{height:79px;border-radius:10px}
.booking-btn{left:26px;top:456px;width:125px;height:42px}

/* welcome */
.welcome-small{left:560px;top:708px;font-size:34px;font-weight:300;color:var(--ink)}
.welcome-big{left:558px;top:740px;font-size:76px;font-weight:700;color:var(--ink);letter-spacing:-.5px}
.para{font-size:12px;line-height:19px;color:var(--body)}
.welcome-p1{left:560px;top:843px;width:540px}
.welcome-p2{left:560px;top:954px;width:540px}
.welcome-btn{left:560px;top:1038px;width:148px;height:42px}

/* services */
.services-small{left:94px;top:1270px;font-size:40px;font-weight:300}
.services-big{left:92px;top:1300px;font-size:84px;font-weight:700;letter-spacing:2px}
.services-p{left:94px;top:1400px;width:362px}
.services-btn{left:94px;top:1521px;width:162px;height:41px}
.card{width:185px;height:411px;box-shadow:0 4px 14px rgba(0,0,0,.15);overflow:hidden}
.card-img{position:absolute;left:0;top:0;width:185px;height:300px}
.card svg{position:absolute;left:0;top:268px}
.card-label{position:absolute;left:0;width:185px;bottom:22px;text-align:center;color:var(--white);font-size:20px;font-weight:300;letter-spacing:.5px}

/* news */
.news-title{top:1782px;left:0;width:1200px;text-align:center;font-size:72px}
.news-title .l{font-weight:300;color:#444}
.news-title .b{font-weight:700}
.news{top:1913px;width:323px}
.news-img{width:323px;height:242px}
.news-date{margin-top:28px;font-size:11px;color:#555;display:flex;align-items:center;gap:8px;letter-spacing:.5px}
.news-h{margin-top:6px;font-size:20px;color:var(--ink)}
.news-p{margin-top:8px;font-size:11.5px;line-height:18px;color:var(--body)}
.slide-arrow{left:1070px;top:2032px;width:36px;height:86px;background:var(--blue);display:flex;align-items:center;justify-content:center}

/* doctors */
.doctors{top:2364px;left:0;width:1200px;height:516px;background:var(--blue)}
.doctors-title{left:0;top:60px;width:1200px;text-align:center;font-size:74px;color:var(--white)}
.doctors-title .l{font-weight:300}
.doctors-title .b{font-weight:700}
.doc{top:166px;width:280px;text-align:center;color:var(--white)}
.doc-photo{margin:0 auto;width:130px;height:130px;border-radius:50%;border:4px solid rgba(255,255,255,.55);background:linear-gradient(180deg,#dbeaf4,#f4f8fb 60%,#c9dbe8)}
.doc-name{margin-top:22px;font-size:20px}
.doc-role{margin-top:1px;font-size:13px;color:rgba(255,255,255,.85)}
.doc-p{margin-top:8px;font-size:11.5px;line-height:18px;color:rgba(255,255,255,.85)}
.doc-arrow{top:253px}

/* location */
.map{left:0;top:2916px;width:784px;height:431px;background:linear-gradient(135deg,#eeeeee,#e2e2e2 50%,#ececec);box-shadow:0 4px 14px rgba(0,0,0,.1)}
.map-pin{left:460px;top:3076px}
.loc-small{right:94px;top:3034px;font-size:38px;font-weight:300;color:#444}
.loc-big{right:92px;top:3068px;font-size:82px;font-weight:700;letter-spacing:-.5px}
.loc-p{right:94px;top:3160px;width:300px;text-align:right}

/* footer */
.footer{top:3386px;left:0;width:1200px;height:249px;background:var(--footer)}
.foot-h{top:75px;font-size:16px;font-weight:500;color:var(--white);letter-spacing:.5px}
.foot-list{top:109px;list-style:none;font-size:11px;color:#b7bcc6}
.foot-list li{height:24px;display:flex;align-items:center;gap:8px}
.foot-list b{color:var(--white);font-weight:500}
.tri{width:0;height:0;border-left:5px solid var(--blue);border-top:3.5px solid transparent;border-bottom:3.5px solid transparent}
.helpline{left:911px;top:109px;font-size:18px;font-weight:300;color:#b7bcc6}
.bottombar{top:3635px;left:0;width:1200px;height:85px;background:var(--blue)}
.bottom-logo{left:94px;top:14px;color:var(--white);font-size:32px}
.copyright{left:94px;top:52px;font-size:10px;color:var(--white)}
.bottom-nav a{position:absolute;top:45px;font-size:12px;color:var(--white);text-decoration:none}
</style>
</head>
<body>

<header>
  <div class="abs topbar">
    <div class="abs topbar-phone">
      <svg width="12" height="12" viewBox="0 0 24 24"><path d="M6.6 10.8a15 15 0 0 0 6.6 6.6l2.2-2.2a1 1 0 0 1 1-.25 11.4 11.4 0 0 0 3.6.6 1 1 0 0 1 1 1V20a1 1 0 0 1-1 1A17 17 0 0 1 3 4a1 1 0 0 1 1-1h3.5a1 1 0 0 1 1 1c0 1.25.2 2.45.6 3.6a1 1 0 0 1-.25 1z" fill="#0392cd"/></svg>
      +0400 555 012
    </div>
  </div>
  <div class="abs logo nav-logo">brivon</div>
  <nav class="abs nav">
    <a class="active" style="left:838px">Home</a>
    <a style="left:908px">Services</a>
    <a style="left:991px">About Us</a>
    <a style="left:1077px">News</a>
  </nav>
</header>

<section class="abs hero" role="img" aria-label="Photo of a smiling young woman in a dental chair beside a dentist in blue gloves"></section>
<div class="abs hero-small">For Happy And</div>
<h1 class="abs hero-big">Healthy Smiles</h1>
<a class="btn btn-blue hero-btn">Make An Appointment</a>
<span class="abs dot on" style="left:572px"></span>
<span class="abs dot" style="left:595px"></span>
<span class="abs dot" style="left:616px"></span>

<form class="abs booking">
  <div class="abs booking-small">Book An</div>
  <div class="abs booking-big">Appointment</div>
  <div class="field" style="top:147px">Name</div>
  <div class="field" style="top:190px">Phone Number</div>
  <div class="field" style="top:232px">Email</div>
  <div class="field" style="top:274px">Date
    <svg style="position:absolute;right:14px;top:9px" width="16" height="16" viewBox="0 0 16 16"><rect x="1" y="2" width="14" height="13" rx="1" fill="none" stroke="#fff" stroke-width="1.3"/><line x1="1" y1="6" x2="15" y2="6" stroke="#fff" stroke-width="1.3"/></svg>
  </div>
  <div class="field" style="top:319px">Time
    <svg style="position:absolute;right:16px;top:15px" width="8" height="5" viewBox="0 0 8 5"><path d="M0 0h8L4 5z" fill="#fff"/></svg>
  </div>
  <div class="field area" style="top:365px">Comment</div>
  <a class="btn btn-white booking-btn">Book A Visit</a>
</form>

<section>
  <div class="abs welcome-small">Welcome to</div>
  <h2 class="abs welcome-big">Brivon Australia</h2>
  <p class="abs para welcome-p1">Lorem ipsum dolor sit amet, consectetur adipiscing elit. Proin vehicula tincidunt vehicula. Etiam vel dictum odio. Donec interdum, libero at dignissim fermentum, elit magna ornare arcu, eget egestas nulla ex at mi. Curabitur mi purus, condimentum sit amet aliquam at, vulputate nec ipsum. Integer lectus lectus, maximus quis felis vel, feugiat elementum ligula. Phasellus ut lectus tellus. Nam vulputate lacinia augue ut scelerisque.</p>
  <p class="abs para welcome-p2">Ut volutpat diam sit amet tincidunt faucibus. Morbi id neque est. Nulla imperdiet congue accumsan. Pellentesque a neque semper, egestas leo vel, sollicitudin nulla. In tristique, neque sed accumsan feugiat, dolor felis ultrices quam, sed fringilla mi libero sagittis magna.</p>
  <a class="btn btn-blue welcome-btn">Know More</a>
</section>

<section>
  <div class="abs services-small">Our</div>
  <h2 class="abs services-big">Services</h2>
  <p class="abs para services-p">Ut volutpat diam sit amet tincidunt faucibus. Morbi id neque est. Nulla imperdiet congue accumsan. Pellentesque a neque semper, egestas leo vel, sollicitudin nulla. In tristique, neque sed accumsan feugiat, dolor felis ultrices quam, sed fringilla mi libero sagittis magna.</p>
  <a class="btn btn-blue services-btn">View All Services</a>

  <div class="abs card" style="left:516px;top:1252px">
    <div class="card-img" role="img" aria-label="Close-up photo of a bright white smile" style="background:linear-gradient(180deg,#e5a69a,#d98d86 50%,#f0e6e4)"></div>
    <svg width="185" height="143" viewBox="0 0 185 143"><path d="M0 22 Q92 -18 185 22 V143 H0z" fill="#0392cd"/><path d="M0 30 Q92 -8 185 30 V143 H0z" fill="#5bb5e0"/></svg>
    <div class="card-label">Teeth Whitening</div>
  </div>
  <div class="abs card" style="left:719px;top:1294px">
    <div class="card-img" role="img" aria-label="Photo of a patient having teeth cleaned under a curing light" style="background:linear-gradient(180deg,#cdb7a8,#8a6a5e 50%,#3a3a44)"></div>
    <svg width="185" height="143" viewBox="0 0 185 143"><path d="M0 22 Q92 -18 185 22 V143 H0z" fill="#0392cd"/><path d="M0 30 Q92 -8 185 30 V143 H0z" fill="#5bb5e0"/></svg>
    <div class="card-label">Teeth Cleaning</div>
  </div>
  <div class="abs card" style="left:921px;top:1252px">
    <div class="card-img" role="img" aria-label="Photo of a smiling dentist in a white coat" style="background:linear-gradient(180deg,#d8dadc,#e9ecef 55%,#f4f6f8)"></div>
    <svg width="185" height="143" viewBox="0 0 185 143"><path d="M0 22 Q92 -18 185 22 V143 H0z" fill="#0392cd"/><path d="M0 30 Q92 -8 185 30 V143 H0z" fill="#5bb5e0"/></svg>
    <div class="card-label">Certified Dentists</div>
  </div>
</section>

<section>
  <h2 class="abs news-title"><span class="l">Latest</span> <span class="b">News</span></h2>
  <article class="abs news" style="left:94px">
    <div class="news-img" role="img" aria-label="Photo of a dentist treating a patient in a clinic" style="background:linear-gradient(135deg,#9aa3ab,#e4e8ec 55%,#c9cfd5)"></div>
    <div class="news-date"><svg width="14" height="13" viewBox="0 0 14 13"><rect width="14" height="13" fill="#0392cd"/><rect x="1.5" y="4" width="11" height="7.5" fill="#fff"/></svg>Aug. 08, 2019</div>
    <h3 class="news-h">Integer dolor est</h3>
    <p class="news-p">Curabitur sit amet sapien nisi. Suspendisse sit amet varius nulla, id sodales nisi. Duis lectus ex, aliquet vitae faucibus at, mollis varius neque...</p>
  </article>
  <article class="abs news" style="left:439px">
    <div class="news-img" role="img" aria-label="Photo of a dental mirror on a pale blue surface" style="background:linear-gradient(160deg,#dfe5ee,#c4ccd8 60%,#a9b3c1)"></div>
    <div class="news-date"><svg width="14" height="13" viewBox="0 0 14 13"><rect width="14" height="13" fill="#0392cd"/><rect x="1.5" y="4" width="11" height="7.5" fill="#fff"/></svg>Aug. 08, 2019</div>
    <h3 class="news-h">Integer dolor est</h3>
    <p class="news-p">Curabitur sit amet sapien nisi. Suspendisse sit amet varius nulla, id sodales nisi. Duis lectus ex, aliquet vitae faucibus at, mollis varius neque...</p>
  </article>
  <article class="abs news" style="left:784px">
    <div class="news-img" role="img" aria-label="Photo of a woman holding her cheek with toothache" style="background:linear-gradient(90deg,#8a6a58,#e6e2de 55%,#f2f2f2)"></div>
    <div class="news-date"><svg width="14" height="13" viewBox="0 0 14 13"><rect width="14" height="13" fill="#0392cd"/><rect x="1.5" y="4" width="11" height="7.5" fill="#fff"/></svg>Aug. 08, 2019</div>
    <h3 class="news-h">Integer dolor est</h3>
    <p class="news-p">Curabitur sit amet sapien nisi. Suspendisse sit amet varius nulla, id sodales nisi. Duis lectus ex, aliquet vitae faucibus at, mollis varius neque...</p>
  </article>
  <div class="abs slide-arrow"><svg width="14" height="34" viewBox="0 0 14 34"><path d="M2 2l10 15L2 32" fill="none" stroke="#fff" stroke-width="1.5"/></svg></div>
</section>

<section class="abs doctors">
  <h2 class="abs doctors-title"><span class="l">Meet Our</span> <span class="b">Doctor</span></h2>
  <svg class="abs doc-arrow" style="left:72px" width="42" height="12" viewBox="0 0 42 12"><path d="M41 6H2M7 1L1 6l6 5" fill="none" stroke="#fff" stroke-width="2"/></svg>
  <svg class="abs doc-arrow" style="left:1086px" width="42" height="12" viewBox="0 0 42 12"><path d="M1 6h39M35 1l6 5-6 5" fill="none" stroke="#fff" stroke-width="2"/></svg>
  <div class="abs doc" style="left:80px">
    <div class="doc-photo" role="img" aria-label="Portrait photo of a female dentist"></div>
    <div class="doc-name">Lorem ipsum</div>
    <div class="doc-role">Dentist-surgeon</div>
    <p class="doc-p">Nullam feugiat placerat rutrum. Etiam quis convallis lacus. Integer quis elit justo. Ut eget lorem at orci maximus finibus non et ligula. In quis nisi leo.</p>
  </div>
  <div class="abs doc" style="left:455px">
    <div class="doc-photo" role="img" aria-label="Portrait photo of a male dentist in a white coat"></div>
    <div class="doc-name">Suspendisse</div>
    <div class="doc-role">Dentist-surgeon</div>
    <p class="doc-p">Nullam feugiat placerat rutrum. Etiam quis convallis lacus. Integer quis elit justo. Ut eget lorem at orci maximus finibus non et ligula. In quis nisi leo.</p>
  </div>
  <div class="abs doc" style="left:829px">
    <div class="doc-photo" role="img" aria-label="Portrait photo of a male dentist in dark scrubs"></div>
    <div class="doc-name">Fusce sodales</div>
    <div class="doc-role">Dentist-surgeon</div>
    <p class="doc-p">Nullam feugiat placerat rutrum. Etiam quis convallis lacus. Integer quis elit justo. Ut eget lorem at orci maximus finibus non et ligula. In quis nisi leo.</p>
  </div>
</section>

<section>
  <div class="abs map" role="img" aria-label="Map showing the clinic location"></div>
  <svg class="abs map-pin" width="32" height="44" viewBox="0 0 32 44"><path d="M16 1C7.7 1 1 7.7 1 16c0 11 15 27 15 27s15-16 15-27C31 7.7 24.3 1 16 1z" fill="#0392cd"/><circle cx="16" cy="16" r="7" fill="#fff"/></svg>
  <div class="abs loc-small">Location of</div>
  <h2 class="abs loc-big">Business</h2>
  <p class="abs para loc-p">Ut volutpat diam sit amet tincidunt faucibus. Morbi id neque est. Nulla imperdiet congue accumsan. Pellentesque a neque semper</p>
</section>

<footer>
  <div class="abs footer">
    <div class="abs foot-h" style="left:94px">Contact Us</div>
    <ul class="abs foot-list" style="left:94px">
      <li><svg width="11" height="11" viewBox="0 0 24 24"><path d="M6.6 10.8a15 15 0 0 0 6.6 6.6l2.2-2.2a1 1 0 0 1 1-.25 11.4 11.4 0 0 0 3.6.6 1 1 0 0 1 1 1V20a1 1 0 0 1-1 1A17 17 0 0 1 3 4a1 1 0 0 1 1-1h3.5a1 1 0 0 1 1 1c0 1.25.2 2.45.6 3.6a1 1 0 0 1-.25 1z" fill="#0392cd"/></svg>+0400 555 012</li>
      <li><svg width="12" height="9" viewBox="0 0 12 9"><rect width="12" height="9" fill="#0392cd"/><path d="M0 0l6 5 6-5" fill="none" stroke="#262a33" stroke-width="1"/></svg>hello@brivon.com.au</li>
      <li><svg width="11" height="11" viewBox="0 0 12 12"><circle cx="6" cy="6" r="5.3" fill="none" stroke="#0392cd" stroke-width="1.2"/><ellipse cx="6" cy="6" rx="2.3" ry="5.3" fill="none" stroke="#0392cd"/><line x1="1" y1="6" x2="11" y2="6" stroke="#0392cd"/></svg>www.brivon.com.au</li>
    </ul>
    <div class="abs foot-h" style="left:383px">Opening Hours</div>
    <ul class="abs foot-list" style="left:383px">
      <li>Monday-Friday: <b>11am-8pm</b></li>
      <li>Weekend: <b>10am-6pm</b></li>
    </ul>
    <div class="abs foot-h" style="left:677px">Our Services</div>
    <ul class="abs foot-list" style="left:677px">
      <li><span class="tri"></span>Teeth Whitening</li>
      <li><span class="tri"></span>Teeth Cleaning</li>
      <li><span class="tri"></span>Quality Brackets</li>
      <li><span class="tri"></span>Certified Dentists</li>
    </ul>
    <div class="abs foot-h" style="left:911px">Other Links</div>
    <div class="abs helpline">24 X 7 Helpline Support</div>
  </div>
  <div class="abs bottombar">
    <div class="abs logo bottom-logo">brivon</div>
    <div class="abs copyright">© 2019 Brivon Australia. All Right Reserved.</div>
    <nav class="bottom-nav">
      <a style="left:828px">Home</a>
      <a style="left:901px">Services</a>
      <a style="left:986px">About Us</a>
      <a style="left:1077px">News</a>
    </nav>
  </div>
</footer>

</body>
</html>
```